Pest Control Company needs business card!

Hi there, we need a business card designed for our new Pest Control Company. Ideally this card will be simple, yet feel elegant and high end. We want to use the colours Orange, Black and White. Please see our attached logo for the exact colours.

Business card details:

Phone - 0461 275 804
Name - Gavin Holloway
Email - Info@steadfastverminguard.com.au

We would also like to include the following list with dot points:

SERVICES / INSPECTIONS

Termites, Wood Borers, Ants, Cockroaches, Spiders, Fleas, Mice, Rats, Bed Bugs, & More!

```html
<!DOCTYPE html>
<html lang="en">
<head>
<meta charset="utf-8">
<title>Steadfast Vermin Guard – Business Card</title>
<link rel="stylesheet" href="https://fonts.googleapis.com/css2?family=Hind:wght@400;600;700&family=Arimo:wght@400;700&display=swap">
<style>
  :root {
    --page-bg: #ebeceb;
    --brand-orange: #ef7f1a;
    --brand-black: #1a1a1a;
    --brand-white: #ffffff;
    --accent-red: #d7262b;
    --text-dark: #231f20;
    --card-shadow: 6px 10px 14px rgba(0, 0, 0, 0.16);
  }
  * { box-sizing: border-box; margin: 0; padding: 0; }
  html, body {
    width: 1004px;
    height: 1200px;
    overflow: hidden;
    background: var(--page-bg);
  }
  .card {
    position: absolute;
    left: 174px;
    width: 656px;
    height: 380px;
    border-radius: 20px;
    box-shadow: var(--card-shadow);
    overflow: hidden;
  }
  .card--front {
    top: 171px;
    background: var(--brand-orange);
  }
  .card--back {
    top: 646px;
    background: var(--brand-white);
  }
  .brand {
    position: absolute;
    display: flex;
    align-items: center;
    gap: 14px;
    font-family: "Hind", sans-serif;
    font-weight: 700;
    font-size: 30px;
    line-height: 0.95;
    text-transform: uppercase;
    letter-spacing: -0.5px;
  }
  .brand__mark {
    width: 70px;
    height: 70px;
    border-radius: 50%;
    flex: none;
  }
  .card--front .brand {
    left: 200px;
    top: 128px;
    color: var(--brand-white);
  }
  .card--front .brand__mark { background: var(--brand-white); }
  .card--back .brand {
    left: 84px;
    top: 136px;
    color: var(--brand-black);
  }
  .card--back .brand__mark { background: var(--brand-black); }
  .services {
    position: absolute;
    left: 0;
    right: 0;
    top: 298px;
    text-align: center;
    font-family: "Hind", sans-serif;
    font-weight: 400;
    font-size: 18.5px;
    line-height: 23px;
    color: var(--brand-white);
  }
  .services__item::before {
    content: "";
    display: inline-block;
    width: 5px;
    height: 5px;
    margin: 0 4px 3px 6px;
    background: var(--brand-white);
    vertical-align: middle;
  }
  .divider {
    position: absolute;
    left: 326px;
    top: 105px;
    width: 3px;
    height: 167px;
    background: var(--accent-red);
  }
  .contact {
    position: absolute;
    left: 350px;
    top: 143px;
    font-family: "Arimo", sans-serif;
    color: var(--text-dark);
  }
  .contact__name {
    font-weight: 700;
    font-size: 17.5px;
    color: var(--accent-red);
    text-transform: uppercase;
    margin-bottom: 14px;
  }
  .contact__line {
    display: flex;
    align-items: center;
    gap: 5px;
    font-size: 17.5px;
    line-height: 27px;
  }
  .contact__icon { width: 10px; height: 10px; flex: none; }
</style>
</head>
<body>
  <section class="card card--front">
    <div class="brand">
      <span class="brand__name">Steadfast<br>Vermin<br>Guard</span>
      <span class="brand__mark"></span>
    </div>
    <p class="services">
      <span class="services__item">Termites</span>
      <span class="services__item">Wood Borers</span>
      <span class="services__item">Ants</span>
      <span class="services__item">Cockroaches</span>
      <span class="services__item">Spiders</span>
      <span class="services__item">Fleas</span><br>
      <span class="services__item">Mice</span>
      <span class="services__item">Rats</span>
      <span class="services__item">Bed Bugs &amp; More!</span>
    </p>
  </section>

  <section class="card card--back">
    <div class="brand">
      <span class="brand__name">Steadfast<br>Vermin<br>Guard</span>
      <span class="brand__mark"></span>
    </div>
    <div class="divider"></div>
    <div class="contact">
      <p class="contact__name">Gavin Holloway</p>
      <p class="contact__line">
        <svg class="contact__icon" viewBox="0 0 10 10" aria-hidden="true">
          <rect x="2.5" y="0.5" width="5" height="9" rx="1" fill="none" stroke="#231f20" stroke-width="1"/>
          <line x1="4" y1="8" x2="6" y2="8" stroke="#231f20" stroke-width="0.8"/>
        </svg>
        0461 275 804
      </p>
      <p class="contact__line">
        <svg class="contact__icon" viewBox="0 0 10 10" aria-hidden="true">
          <rect x="0.5" y="2" width="9" height="6.5" fill="none" stroke="#231f20" stroke-width="1"/>
          <polyline points="0.5,2 5,6 9.5,2" fill="none" stroke="#231f20" stroke-width="1"/>
        </svg>
        Info@steadfastverminguard.com.au
      </p>
    </div>
  </section>
</body>
</html>
```